Health & Nutrition - Business Cards

Needs to look new-age, simple, and elegant. The cards are for my services/counsel in health and nutrition - which include mind, body, and soul. I would like to see something clean and simple but beautiful. Can have a plain background or with a pattern but I don't want it to take away from my contact details. Therefore, my info can be on the back of the card and a nice front design. I really like the flower of life symbol. The name of my business is called Velvet Meadow.

Target Market(s)

Clients - men & women age 20-60. Adults, parents, teachers, sick individuals seeking nutrient counseling and dietary management.

Industry/Entity Type

Nutritionist

Contact Information for Business Card

Tomas Brindle
Cell: 345-827-4602
Email: tbrindle@quillpost.example

Colors
33a6d7
33b8a4
add136
ffffff
5c5c5c
f04a50
fbee3f
cedeed
85cae6

Requirements
Nice to have
• Maybe it can have some sort of sacred geometry as well, but not required. Nice to have the colors that I choose in the project but feel free to come up with your own use of colors. Thanks! =)

```html
<!DOCTYPE html>
<html lang="en">
<head>
<meta charset="utf-8">
<title>Velvet Meadow – Business Card</title>
<link rel="stylesheet" href="https://fonts.googleapis.com/css2?family=Didact+Gothic&display=swap">
<style>
  :root {
    --olive: #9a9a33;
    --olive-light: #a9aa37;
    --lime: #c5cc2c;
    --ink: #111111;
    --paper: #ffffff;
    --mist: #f1f1f1;
  }
  html, body {
    margin: 0;
    padding: 0;
    width: 912px;
    height: 1200px;
    overflow: hidden;
    background: var(--paper);
  }
  .sheet {
    position: relative;
    width: 912px;
    height: 1200px;
    font-family: "Didact Gothic", "Century Gothic", sans-serif;
    color: var(--ink);
  }
  .card-front {
    position: absolute;
    left: 0;
    top: 0;
    width: 912px;
    height: 600px;
    background: var(--olive);
    overflow: hidden;
  }
  .card-back {
    position: absolute;
    left: 0;
    top: 600px;
    width: 912px;
    height: 600px;
    background: var(--paper);
    overflow: hidden;
  }
  .motif {
    position: absolute;
    left: 0;
    top: 0;
  }
  .brand-name {
    position: absolute;
    left: 324px;
    top: 252px;
    margin: 0;
    font-weight: 400;
    font-size: 78px;
    line-height: 1;
    letter-spacing: -1px;
    color: var(--paper);
    white-space: nowrap;
  }
  .person-name {
    position: absolute;
    left: 76px;
    top: 100px;
    margin: 0;
    font-weight: 400;
    font-size: 48px;
    line-height: 1;
    letter-spacing: -1px;
    white-space: nowrap;
  }
  .person-name .first { color: var(--lime); }
  .person-name .last { color: var(--ink); }
  .contact {
    position: absolute;
    left: 88px;
    top: 476px;
    margin: 0;
    font-style: normal;
  }
  .contact .phone {
    display: block;
    font-size: 36px;
    line-height: 40px;
    letter-spacing: 0.5px;
  }
  .contact .email {
    display: block;
    font-size: 29px;
    line-height: 36px;
    letter-spacing: -0.5px;
  }
</style>
</head>
<body>
<main class="sheet">
  <section class="card-front">
    <svg class="motif" width="912" height="600" viewBox="0 0 912 600" role="img" aria-label="Flower of life sacred geometry pattern in lime line work">
      <circle cx="0" cy="299" r="282" fill="var(--olive-light)"/>
    </svg>
    <h1 class="brand-name">Velvet Meadow</h1>
  </section>

  <section class="card-back">
    <svg class="motif" width="912" height="600" viewBox="0 0 912 600" role="img" aria-label="Faint grey flower of life sacred geometry pattern">
      <circle cx="914" cy="302" r="262" fill="var(--mist)"/>
    </svg>
    <h2 class="person-name"><span class="first">TOMAS</span><span class="last">BRINDLE</span></h2>
    <address class="contact">
      <span class="phone">345-827-4602</span>
      <span class="email">tbrindle@quillpost.example</span>
    </address>
  </section>
</main>
</body>
</html>
```